New Business Card Design Project - RK Ledgerwise & Filing Partners, LLC

Below is a sample image of the card (TM Bookkeeping). I would like to have a designed business card that looks very similar (Front & Back). In addition, I would like to keep the same colors as well. I attached my Business Logo (RK Ledgerwise & Filing Partners, LLC) that will be on my website.

Target Market(s)

Executives, Business Owners, Board of Directors, Chief Financial Officers

Contact Information for Business Card

Font styles to use
Serif

Colors
0c5ba6
ffffff
5c5c5c

Requirements
Must have
• My Name: Malcolm Ferris, CPA
• Position: Owner
• Phone: (240) 555-0148
• Email: Mferris@rkledgerwise.example
• Website: www.Rkledgerwise.example
• Address: 4736 Ferncliff Ave #2093
• Dunmore Falls, MD 21990
Nice to have
• Same design & color scheme as TM Bookkeepnig Business card sample attached

```html
<!DOCTYPE html>
<html lang="en">
<head>
<meta charset="utf-8">
<title>RK Ledgerwise &amp; Filing Partners – Business Card</title>
<link rel="stylesheet" href="https://fonts.googleapis.com/css2?family=Tinos:wght@400;700&display=swap">
<style>
  :root {
    --brand-blue: #15b1e1;
    --brand-grey: #6b6b6b;
    --text-grey: #5c5c5c;
    --paper: #ffffff;
    --backdrop-inner: #5c5b5c;
    --backdrop-outer: #0d0d0d;
  }
  * { margin: 0; padding: 0; box-sizing: border-box; }
  html, body { width: 1200px; height: 999px; overflow: hidden; }
  body {
    position: relative;
    background: radial-gradient(ellipse 62% 62% at 50% 50%, var(--backdrop-inner) 0%, #3d3c3d 60%, var(--backdrop-outer) 100%);
    font-family: "Tinos", "Times New Roman", serif;
  }
  .card {
    position: absolute;
    left: 206px;
    width: 787px;
    height: 450px;
    overflow: hidden;
  }
  .card-front { top: 37px; background: var(--paper); }
  .card-back  { top: 511px; background: var(--brand-blue); }

  .front-wordmark {
    position: absolute;
    left: 0; width: 388px;
    top: 236px;
    text-align: center;
    color: var(--brand-blue);
    font-size: 31px;
    line-height: 34px;
    letter-spacing: 1.5px;
    text-transform: uppercase;
  }
  .divider {
    position: absolute;
    left: 377px; top: 95px;
    width: 2px; height: 254px;
    background: linear-gradient(to bottom, rgba(107,107,107,0), var(--brand-grey) 15%, var(--brand-grey) 85%, rgba(107,107,107,0));
  }
  .contact {
    position: absolute;
    left: 464px; top: 96px;
    color: var(--text-grey);
  }
  .contact-name {
    color: var(--brand-blue);
    font-weight: 700;
    font-size: 24px;
    line-height: 28px;
  }
  .contact-role { font-size: 17px; margin-top: 8px; }
  .contact-address { font-size: 17px; line-height: 23px; margin-top: 23px; }
  .contact-list { list-style: none; margin-top: 22px; font-size: 17px; }
  .contact-list li { display: flex; align-items: center; height: 28.5px; }
  .contact-icon { width: 18px; height: 18px; margin-right: 21px; flex: none; }
  .front-band { position: absolute; left: 0; top: 0; width: 787px; height: 450px; }

  .back-wordmark {
    position: absolute;
    left: 0; right: 0;
    top: 263px;
    text-align: center;
    color: var(--paper);
    font-size: 44px;
    line-height: 46px;
    letter-spacing: 2px;
    text-transform: uppercase;
  }
</style>
</head>
<body>
  <section class="card card-front" aria-label="Card front">
    <svg class="front-band" viewBox="0 0 787 450" aria-hidden="true">
      <rect x="0" y="398" width="420" height="20" fill="var(--brand-grey)"/>
      <path d="M0 418 H350 C385 418 392 377 438 377 H787 V450 H0 Z" fill="var(--brand-blue)"/>
    </svg>

    <p class="front-wordmark">RK Ledgerwise<br>&amp; Filing Partners</p>
    <div class="divider"></div>

    <div class="contact">
      <h1 class="contact-name">Malcolm Ferris, CPA</h1>
      <p class="contact-role">Owner</p>
      <p class="contact-address">4736 Ferncliff Ave #2093<br>Dunmore Falls, MD 21990</p>
      <ul class="contact-list">
        <li>
          <svg class="contact-icon" viewBox="0 0 18 18" aria-hidden="true">
            <rect width="18" height="18" rx="3" fill="var(--brand-blue)"/>
            <path d="M6 4 L8 4 L8.6 7 L7.4 8 C8 9.6 8.8 10.4 10 11 L11 9.8 L14 10.4 L14 12.4 C14 13.2 13.4 13.6 12.6 13.6 C8.2 13.2 4.8 9.8 4.4 5.4 C4.4 4.6 5 4 6 4 Z" fill="var(--paper)"/>
          </svg>
          <span>(240) 555-0148</span>
        </li>
        <li>
          <svg class="contact-icon" viewBox="0 0 18 18" aria-hidden="true">
            <path d="M1 7 L9 1.5 L17 7 V16 H1 Z" fill="var(--brand-blue)"/>
            <path d="M2.5 8 L9 12 L15.5 8" fill="none" stroke="var(--paper)" stroke-width="1.4"/>
          </svg>
          <span>Mferris@rkledgerwise.example</span>
        </li>
        <li>
          <svg class="contact-icon" viewBox="0 0 18 18" aria-hidden="true">
            <path d="M6 1.5 C6.8 1.5 7.4 2 7.4 2.8 V8 L12.6 9 C13.6 9.2 14.2 10 14 11 L13.2 15.5 C13 16.3 12.4 17 11.5 17 H7.6 C7 17 6.5 16.7 6.2 16.2 L3 11.4 C2.6 10.8 2.8 10 3.4 9.6 C4 9.2 4.6 9.4 4.6 9.4 V2.8 C4.6 2 5.2 1.5 6 1.5 Z" fill="var(--brand-blue)"/>
          </svg>
          <span>www.Rkledgerwise.example</span>
        </li>
      </ul>
    </div>
  </section>

  <section class="card card-back" aria-label="Card back">
    <p class="back-wordmark">RK Ledgerwise<br>&amp; Filing Partners</p>
  </section>
</body>
</html>
```